Lorvika.no is a new website about pedagogical entrepreneurship. It's main target group is teachers. The Fjellmark Institute for Classroom Media and the Nordvik Agency for Schools and Study are leading the project.

The web page is meant to show examples of how different methods of entrepreneurship can be used pedagogical in a learning environment. The page will also support the user with examples of different teaching programs and other examples of best practice.

Pedagogical entrepreneurship is not about business and men in suits. It's a method for learning. The focus in the design should be on school, education and new ways of learning.

The final product should be motivating and engaging, but at the same time governmental and serious. We are not looking for something "flashy" and corporate-looking, but a moderate, task-focused and clean design that state quality.

We need designs for three pages:
1 - frontpage
2 - subpage ("Metoder og undervisningsopplegg")
3 - subpage ("Smått-VERK i Brekkelia")

The interaction design for these three pages will be uploaded as an attachment.

We would like you to find inspiration in the following websites:
- www.gryvekst.no
- www.lavrek.no
- www.tovandstudio.com
- www.kvp.no
(more will be added)

Please use the attached logo, and feel free to use this as an inspiration for the rest of the design.

Target Market(s)

Teachers

Industry/Entity Type

Education

Requirements
Must have
• * Header with: Logo. Main navigation. Utility navigation. Search box.
* Footer
Should not have
• Images of men in suits.
Very strong graphical elements that stands out too much (we want it clean).

```html
<!DOCTYPE html>
<html lang="en">
<head>
<meta charset="utf-8">
<title>Lorvika.no – Pedagogical Entrepreneurship</title>
<link rel="stylesheet" href="https://fonts.googleapis.com/css2?family=Cabin:wght@400;500;600;700&family=Alegreya+Sans+SC:wght@800&family=Shadows+Into+Light&family=Signika:wght@400;600&display=swap">
<style>
:root{
  --page-bg:#d3e5f0;
  --card:#ffffff;
  --ink:#2b2b2b;
  --link:#2f6d99;
  --accent:#3d9ad6;
  --accent-light:#8fd0f3;
  --tag:#bfe2f5;
  --hero-dark:#1e5f8e;
  --hero-light:#5ab0e0;
  --footer:#262626;
  --footer-bar:#1b1b1b;
  --pink:#e2308c;
}
*{box-sizing:border-box;margin:0;padding:0}
html,body{width:1094px;height:1200px;overflow:hidden}
body{background:linear-gradient(180deg,#d6e9f4,#cfe1ec);font-family:"Cabin",sans-serif;color:var(--ink);position:relative}
.site{position:absolute;left:64px;top:46px;width:966px;height:1100px;background:var(--card);border-radius:8px;overflow:hidden}
a{color:inherit;text-decoration:none}

.utility-nav{position:absolute;top:12px;left:0;width:100%;font-size:13px;color:var(--link)}
.utility-nav a{position:absolute}
.brand{position:absolute;left:41px;top:38px;display:flex;align-items:center;gap:10px}
.brand-mark{width:34px;height:34px;border-radius:50%;background:var(--accent)}
.brand-name{font-family:"Signika",sans-serif;font-weight:600;font-size:30px;color:var(--accent)}
.search{position:absolute;left:734px;top:44px;width:193px;height:28px;border:1px solid #9aa4ab;border-radius:3px;display:flex;overflow:hidden}
.search input{flex:1;border:0;outline:0}
.search button{width:36px;border:0;background:linear-gradient(#3b7fb8,#1d5689);display:flex;align-items:center;justify-content:center}

.hero{position:absolute;left:38px;top:91px;width:889px;height:305px;overflow:hidden;
  background:radial-gradient(ellipse at 55% 110%,#5aaedd 0%,#3a8cc4 35%,#23679a 75%,#1c5786 100%)}
.hero-art{position:absolute;right:0;top:40px;width:260px;height:265px;background:linear-gradient(160deg,rgba(255,255,255,.85),rgba(255,255,255,.35));border-radius:120px 0 0 0}
.ribbon{position:absolute;right:-44px;top:22px;width:180px;height:28px;background:var(--pink);transform:rotate(40deg);color:#fff;font:700 20px "Cabin",sans-serif;text-align:center;line-height:28px;letter-spacing:1px}
.hero-title{position:absolute;left:56px;top:70px;font-family:"Alegreya Sans SC",sans-serif;font-weight:800;font-size:52px;line-height:54px;color:#fff;text-shadow:0 2px 3px rgba(0,0,0,.35)}
.hero-sub{position:absolute;left:226px;top:197px;width:360px;font-size:18px;line-height:30px;font-style:italic;color:#fff}
.learn-more{position:absolute;left:577px;top:224px;width:320px;height:60px;background:rgba(20,30,40,.78);text-align:right;padding:6px 14px 0 0}
.learn-more strong{display:block;font-size:25px;color:#fff;font-weight:600;line-height:30px}
.learn-more span{font-family:"Shadows Into Light",cursive;color:var(--accent-light);font-size:16px}

.main-nav{position:absolute;left:237px;top:91px;width:486px;height:51px;background:#fff;border-radius:0 0 6px 6px;box-shadow:0 2px 4px rgba(0,0,0,.2);display:flex;align-items:center;padding:0 10px;font-size:12.5px;font-weight:600;line-height:15px}
.main-nav a{display:flex;align-items:center;gap:9px;padding:0 14px;border-right:1px solid #bbb}
.main-nav a:last-child{border:0}
.main-nav .first{color:var(--link)}
.nav-icon{width:26px;height:26px;flex:none}

.meter{position:absolute;left:110px;top:334px;width:130px;height:130px;border-radius:50%;background:#fff;box-shadow:0 2px 6px rgba(0,0,0,.35);display:flex;align-items:center;justify-content:center}
.meter-face{width:112px;height:112px;border-radius:50%;background:radial-gradient(circle at 50% 35%,#37a8f0,#0b6fc4)}
.meter-question{position:absolute;left:89px;top:480px;font-size:18px;line-height:21px;font-style:italic;color:var(--accent)}
.meter-button{position:absolute;left:91px;top:520px;width:169px;height:33px;border:1px solid #999;border-radius:4px;background:linear-gradient(#efefef,#c9c9c9);font:600 15px "Cabin",sans-serif;color:#222}

.tag-group{position:absolute;top:438px;width:260px}
.tag-group h2{font:500 20px "Cabin",sans-serif;color:#333;margin-bottom:7px}
.tag-group .more{position:absolute;right:0;top:7px;font-size:10.5px;font-weight:600;color:var(--link)}
.tags{display:flex;flex-wrap:wrap;gap:6px 5px}
.tags span{background:var(--tag);height:27px;line-height:27px;padding:0 9px;font-family:"Signika",sans-serif;font-size:14px;color:#333}
.divider{position:absolute;left:41px;top:585px;width:884px;border-top:1px solid #c4c4c4}

.inspiration h2{position:absolute;left:0;width:100%;top:624px;text-align:center;font-size:20px;font-weight:600;color:var(--link)}
.story{position:absolute;top:665px;width:209px;height:168px;background:#fff;box-shadow:0 1px 5px rgba(0,0,0,.3);padding:7px}
.story-photo{height:130px;background:linear-gradient(180deg,#c9cdd1 0%,#8e8f86 45%,#6d6a58 60%,#e4e8ee 80%,#f2f4f6 100%)}
.story p{font-size:11.5px;font-weight:600;margin-top:6px;color:#333}
.arrow{position:absolute;top:773px;width:38px;height:38px;border-radius:50%;background:linear-gradient(#fff,#ddd);box-shadow:0 1px 3px rgba(0,0,0,.35);color:#999;font-size:16px;text-align:center;line-height:36px;font-weight:700}

.footer{position:absolute;left:0;top:876px;width:966px;height:224px;background:linear-gradient(#2c2c2c,#1f1f1f);color:#fff}
.footer-mark{position:absolute;left:58px;top:42px;width:70px;height:70px;border-radius:50%;background:var(--accent)}
.footer-col{position:absolute;top:30px;font-size:13.5px;line-height:22.5px}
.footer-col h3{font-size:18px;font-weight:600;color:var(--accent-light);line-height:24px;margin-bottom:1px}
.footer-col a{display:block}
.footer-col .see{text-decoration:underline}
.footer-bar{position:absolute;left:0;bottom:0;width:100%;height:46px;background:linear-gradient(#3a3a3a,#141414);text-align:center;line-height:46px;font-size:17px;font-weight:600}
.footer-bar span{color:var(--accent-light)}
</style>
</head>
<body>
<div class="site">
  <nav class="utility-nav">
    <a href="#" style="left:542px">Best Practice School</a>
    <a href="#" style="left:700px">Lorvimeter</a>
    <a href="#" style="left:825px">About Lorvika.no</a>
  </nav>

  <a class="brand" href="#"><span class="brand-mark"></span><span class="brand-name">Lorvika</span></a>

  <form class="search">
    <input type="text" aria-label="Search">
    <button type="button" aria-label="Search">
      <svg width="14" height="14" viewBox="0 0 14 14"><circle cx="5.5" cy="5.5" r="3.8" fill="none" stroke="#fff" stroke-width="2"/><line x1="8.5" y1="8.5" x2="12.5" y2="12.5" stroke="#fff" stroke-width="2.4" stroke-linecap="round"/></svg>
    </button>
  </form>

  <section class="hero">
    <div class="hero-art" role="img" aria-label="White flower and playful creature illustration"></div>
    <div class="ribbon">FREE</div>
    <h1 class="hero-title">Pedagogical<br>Entrepreneurship<br>Works</h1>
    <p class="hero-sub">Studying won’t be just sitting behind the desk and read books anymore.</p>
    <a class="learn-more" href="#"><strong>LEARN MORE!</strong><span>explore one of the best learning method ever</span></a>
  </section>

  <nav class="main-nav">
    <a href="#" class="first"><svg class="nav-icon" viewBox="0 0 26 26"><circle cx="13" cy="13" r="11" fill="var(--accent)"/></svg>What is pedagogical<br>enterpreneurship ?</a>
    <a href="#"><svg class="nav-icon" viewBox="0 0 26 26"><g fill="#111"><circle cx="13" cy="13" r="9"/><rect x="11" y="1" width="4" height="24"/><rect x="1" y="11" width="24" height="4"/><rect x="11" y="1" width="4" height="24" transform="rotate(45 13 13)"/><rect x="11" y="1" width="4" height="24" transform="rotate(-45 13 13)"/></g><circle cx="13" cy="13" r="5" fill="#fff"/></svg>Method and<br>teaching plans</a>
    <a href="#"><svg class="nav-icon" viewBox="0 0 26 26"><path fill="#111" d="M3 8h6a3 3 0 1 1 6 0h6v6a3 3 0 1 0 0 6v4H3v-5a3 3 0 1 0 0-6z"/></svg>Good Example/<br>Best Practice</a>
  </nav>

  <div class="meter"><div class="meter-face">
    <svg width="112" height="112" viewBox="0 0 112 112"><path d="M30 74a30 30 0 1 1 52 0" fill="none" stroke="#fff" stroke-width="6" stroke-linecap="round"/><line x1="56" y1="64" x2="78" y2="42" stroke="#fff" stroke-width="6" stroke-linecap="round"/><circle cx="56" cy="64" r="8" fill="#fff"/></svg>
  </div></div>
  <p class="meter-question">Are you working<br>enterpreneurship-like?</p>
  <button class="meter-button" type="button">Try the lorvimeter!</button>

  <section class="tag-group" style="left:336px">
    <h2>Methods</h2><a class="more" href="#">+ More</a>
    <div class="tags"><span>Cafe-pedagogikk</span><span>Elevbedrift</span><span>Grundercamp</span><span>Story line</span><span>REAL</span></div>
  </section>
  <section class="tag-group" style="left:639px">
    <h2>Teaching Plans</h2><a class="more" href="#">+ More</a>
    <div class="tags"><span>1st Project Learning</span><span>Forest Tour</span><span>Startup Company</span></div>
  </section>

  <hr class="divider">

  <section class="inspiration">
    <h2>Inspiration</h2>
    <a class="arrow" href="#" style="left:82px">«</a>
    <article class="story" style="left:141px"><div class="story-photo" role="img" aria-label="Schoolyard in winter with a bare tree and students at a building"></div><p>Smått-VERK at Brekkelia School</p></article>
    <article class="story" style="left:375px"><div class="story-photo" role="img" aria-label="Schoolyard in winter with a bare tree and students at a building"></div><p>Smått-VERK at Brekkelia School</p></article>
    <article class="story" style="left:608px"><div class="story-photo" role="img" aria-label="Schoolyard in winter with a bare tree and students at a building"></div><p>Smått-VERK at Brekkelia School</p></article>
    <a class="arrow" href="#" style="left:850px">»</a>
  </section>

  <footer class="footer">
    <div class="footer-mark"></div>
    <div class="footer-col" style="left:146px"><h3>Pedagonal Enterpreneurship</h3><a href="#">What is pedagonal enterpreneurship?</a><a href="#">Science</a><a href="#">Best practice schools</a><a href="#">Lorvimeter</a></div>
    <div class="footer-col" style="left:424px"><h3>Methods</h3><a href="#">Story line</a><a href="#">REAL</a><a href="#">Cafe-pedagoikk</a><a class="see" href="#">See more...</a></div>
    <div class="footer-col" style="left:569px"><h3>Teaching Plans</h3><a href="#">1st Project Learning</a><a href="#">Forest Tour</a><a href="#">Startup Company</a><a class="see" href="#">See more...</a></div>
    <div class="footer-col" style="left:744px"><h3>Gode Eksampler</h3><a href="#">Smått-Verk at Brekkelia School</a><a href="#">Smått-Verk at Brekkelia School</a><a href="#">Smått-Verk at Brekkelia School</a><a class="see" href="#">See more...</a></div>
    <div class="footer-bar">About <span>Lorvika.no</span></div>
  </footer>
</div>
</body>
</html>
```